Brochure Design Project for Brockwell and Daughter Lumber

We are after an executive high-end trifold brochure to be sent to new customers. Please refer to document attached ('brochure notes') for the details.

Target Market(s)

Renovators, Wives, Architects, Builders

Requirements
Must have
• Back of brochure must have a map and contact details.

Must relate to the feel of our website ... brockwellanddaughterlumber.net

Nice to have
• A unique design - something unlike regular brochures.

Developed using Adobe Photoshop or InDesign

```html
<!DOCTYPE html>
<html lang="en">
<head>
<meta charset="utf-8">
<title>Brockwell and Daughter Lumber – Trifold Brochure</title>
<link href="https://fonts.googleapis.com/css2?family=Lora:ital,wght@1,700&family=Tenor+Sans&display=swap" rel="stylesheet">
<style>
:root{
  --page-bg:#ffffff;
  --paper-light:#efe7da;
  --paper-dark:#d9ccb6;
  --band:#8d7c67;
  --band-dark:#7a6a56;
  --ink:#5b4a39;
  --ink-soft:#6e5d4b;
  --cream:#f6f0e6;
  --brand-green:#8fd12c;
  --fold:#c9baa2;
}
*{box-sizing:border-box;margin:0;padding:0}
html,body{width:1200px;height:1000px;overflow:hidden;background:var(--page-bg)}
body{position:relative;font-family:"Tenor Sans",sans-serif;color:var(--ink)}
.sheet{position:absolute;left:30px;width:1140px;height:470px;display:flex;box-shadow:0 2px 8px rgba(0,0,0,.18)}
.sheet--outside{top:15px}
.sheet--inside{top:510px}
.panel{position:relative;width:380px;height:470px;overflow:hidden;
  background:linear-gradient(180deg,var(--paper-light),var(--paper-dark));
  border-right:1px solid var(--fold)}
.panel:last-child{border-right:none}
.band{position:absolute;left:0;right:0;background:var(--band);color:var(--cream)}
.photo{position:absolute;border:3px solid #fff;box-shadow:0 2px 6px rgba(0,0,0,.35)}
.photo--kitchen{background:linear-gradient(180deg,#6f7a70 0%,#cfcfc8 45%,#a5602a 60%,#6b3613 100%)}
.photo--kitchen-bright{background:linear-gradient(180deg,#e2e2de 0%,#b8b6b0 40%,#c07634 62%,#7a3d12 100%)}
.photo--waterfront{background:linear-gradient(160deg,#3f7fb0 0%,#2c5f86 35%,#4b7a3a 55%,#8a6a5f 75%,#a57c6c 100%)}
.photo--deck{background:linear-gradient(135deg,#7a3a1c 0%,#a9542a 40%,#5b2a14 70%,#c9b79a 100%)}
.photo--fence{background:linear-gradient(180deg,#2f64c4 0%,#8fb5e6 45%,#a9663f 60%,#5c8a3c 80%,#79a14e 100%)}
.photo--slat-fence{background:linear-gradient(160deg,#dfe3e6 0%,#8b9298 35%,#a55a3e 60%,#8c4a33 100%)}
.map{position:absolute;background:linear-gradient(135deg,#e7e7e4,#d6d8d3 50%,#e3e3df);border:2px solid #fff}
h2{font-family:"Lora",serif;font-style:italic;font-weight:700;text-transform:uppercase;letter-spacing:.5px}
p,li{font-size:11.5px;line-height:1.35}
.wordmark{font-family:"Tenor Sans",sans-serif;color:var(--brand-green);text-align:center;line-height:1.1}

/* outside left */
.flooring .photo--kitchen{left:18px;top:12px;width:200px;height:135px}
.flooring .band{top:155px;height:188px;padding:9px 16px}
.flooring h2{font-size:13px;color:#fff;margin-bottom:7px;line-height:1.3}
.flooring p{color:var(--cream);text-align:justify;margin-bottom:6px;font-size:10.5px;line-height:1.3}
.flooring .photo--kitchen-bright{left:18px;top:352px;width:200px;height:106px}

/* outside middle */
.contact .map{left:18px;top:15px;width:200px;height:215px}
.contact .band{top:240px;height:95px;padding-top:14px;font-size:12px;line-height:1.3;text-align:center}
.contact .address{width:250px;margin-left:25px}
.contact .web{position:absolute;top:345px;left:25px;width:250px;text-align:center;font-size:12px}
.contact .wordmark{position:absolute;top:385px;left:30px;width:240px;font-size:22px}

/* outside right */
.cover .wordmark{position:absolute;top:70px;left:20px;width:340px;font-size:28px}
.cover .photo--waterfront{left:30px;top:165px;width:215px;height:180px}

/* inside left */
.composite{padding:22px 20px}
.composite h2{font-size:14px;text-align:center;margin-bottom:14px}
.composite .intro{text-align:justify;margin-bottom:10px}
.composite .callout{font-weight:700;font-size:11.5px;color:var(--ink);padding-left:10px;text-indent:-10px}
.composite .band{top:165px;height:160px;padding:14px 18px}
.composite .band h2{color:#fff;font-size:13px;margin-bottom:12px}
.composite .band p{text-align:justify}
.composite .photo--fence{left:18px;top:300px;width:260px;height:155px}

/* inside middle */
.tonka .photo--deck{left:20px;top:20px;width:250px;height:145px}
.tonka .band{top:165px;height:160px;padding:10px 20px}
.tonka .band h2{color:#fff;font-size:13px;text-align:center;margin-bottom:10px}
.tonka .band p{font-size:9.5px;line-height:1.3;margin-bottom:3px}
.tonka .benefits{position:absolute;top:332px;left:20px;right:20px;color:var(--ink-soft)}
.tonka .benefits h3{font-weight:400;font-size:10px;text-transform:uppercase;margin-bottom:6px}
.tonka ul{list-style:none}
.tonka li{font-size:9.5px;line-height:1.3;padding-left:10px;text-indent:-10px}
.tonka li::before{content:"•  "}

/* inside right */
.offer .photo--waterfront{left:20px;top:14px;width:220px;height:132px}
.offer .band{top:165px;height:160px}
.offer .cash-box{position:absolute;top:156px;left:8px;width:250px;height:172px;border:1px solid var(--cream);border-radius:14px;padding:9px 14px;color:#fff;background:rgba(255,255,255,.08)}
.offer .cash-box h2{text-align:center;font-size:13px;margin-bottom:6px}
.offer .cash-box li{list-style:none;font-family:"Lora",serif;font-style:italic;font-weight:700;font-size:10.5px;line-height:1.3;padding-left:8px;text-indent:-8px}
.offer .cash-box li::before{content:"* "}
.offer .photo--slat-fence{left:20px;top:337px;width:220px;height:120px}
</style>
</head>
<body>

<section class="sheet sheet--outside">
  <article class="panel flooring">
    <div class="photo photo--kitchen" role="img" aria-label="Kitchen with polished timber floorboards"></div>
    <div class="band">
      <h2>Traditional Timber and<br>Bamboo Flooring</h2>
      <p>Timber flooring is a natural, environmentally friendly option that can add real value to your home. We can simply supply to DIY-ers or can organise install, sand and finishing.</p>
      <p>Bamboo flooring is becoming an increasingly popular choice for many homeowners, architects, builders and interior designers who are looking for an environmental alternative to timber flooring that is a stylish, hard wearing, pre-finished flooring system.</p>
    </div>
    <div class="photo photo--kitchen-bright" role="img" aria-label="Bright kitchen with glossy timber floor"></div>
  </article>

  <article class="panel contact">
    <div class="map" role="img" aria-label="Street map showing the yard location"></div>
    <div class="band">
      <p class="address">27 Ridgeline Crescent Fernvale<br>Brisbane, Queensland<br>Australia 4306<br>Phone +61 7 3000 4821</p>
    </div>
    <p class="web">www.brockwellanddaughterlumber.net</p>
    <div class="wordmark">Brockwell and Daughter Lumber</div>
  </article>

  <article class="panel cover">
    <div class="wordmark">Brockwell and Daughter Lumber</div>
    <div class="photo photo--waterfront" role="img" aria-label="Waterfront timber deck with built-in bench"></div>
  </article>
</section>

<section class="sheet sheet--inside">
  <article class="panel composite">
    <h2>Composite Timber</h2>
    <p class="intro">Timber decks and screening are very popular but require constant maintenance. This timber-like product gives the look of timber, but with minimal upkeep.</p>
    <p class="callout">• The ‘greenest of green’ … This timber-like product will give you the look you’re after, without needing to oil …. EVER!</p>
    <div class="band">
      <h2>Feature Fencing</h2>
      <p>We are able to supply you with designer fencing fully installed for much less than you think. Endless combinations available. Call for an obligation-free quote today.</p>
    </div>
    <div class="photo photo--fence" role="img" aria-label="Rendered pillar fence with horizontal timber slats"></div>
  </article>

  <article class="panel tonka">
    <div class="photo photo--deck" role="img" aria-label="Close view of reddish-brown hardwood decking"></div>
    <div class="band">
      <h2>Tonka Timber</h2>
      <p>The products include decking, flooring, structural timber and step treads.</p>
      <p>Tonka flooring is warm reddish-brown or purplish-brown with lighter streaks and on exposure gradually becomes uniform light brown.</p>
      <p>It doesn’t bleed like merbau which is ideal around wet areas. Further it carries independent ‘Forest Certified Pure’ certification that it is sourced from 100% legal and well-managed forests.</p>
    </div>
    <div class="benefits">
      <h3>Benefits of the Tonka timber species:</h3>
      <ul>
        <li>Durability Class 1 – no need to treat with nasty chemicals</li>
        <li>Environmentally sustainable – fully certified</li>
        <li>Strong</li>
        <li>Beautiful</li>
        <li>Wide range of uses available – decking, step treads, posts, joists.</li>
      </ul>
    </div>
  </article>

  <article class="panel offer">
    <div class="photo photo--waterfront" role="img" aria-label="Waterfront timber deck with built-in bench"></div>
    <div class="band"></div>
    <div class="cash-box">
      <h2>Want Cash?</h2>
      <ul>
        <li>Become a renovation star! If you allow us to take photos, video or leave a sign, we will reward you with $50 cash for every order taken from interest in your home improvement.</li>
        <li>We can come to you for free measure and quote.</li>
        <li>Design advise</li>
        <li>Can organize full installation.</li>
      </ul>
    </div>
    <div class="photo photo--slat-fence" role="img" aria-label="Modern house with red timber slat fence"></div>
  </article>
</section>

</body>
</html>
```